SALT PAN COMPUTERS AD DESIGN

This is to go into our local phone book as a full page (A4) advert.

NOTE THAT THE DEADLINE IS MIDNIGHT SUNDAY THE 29TH AUSSIE WA TIME NOT THE ADVERTISED DEADLINE AS FOR THE LIFE OF ME I CANT SEE WHERE TO CHANGE IT.

HAPPY TO PAY EXTRA FOR A "YES THATS IT" JOB.

Title - SALT PAN COMPUTERS

(THINGS TO HAVE)
24/7 FULL COMPUTER SERVICES
ALL COMPUTER PROBLEMS SOLVED
info@saltpancomputers.com.au
0400 13 8562
SALTPANCOMPUTERS.COM.AU
Virus's Removed
Data Recovery
Custom Computers and Programs built
Picked up & Dropped off
Private and Business Welcome

Maybe this photo - http://www.pixelvaultlib.com/stock-photo-22810457-attractive-receptionist.php?st=a3e91f2
with 24/7 service.

http://www.pixelvaultlib.com/stock-photo-22936104-hard-disk-drive-service.php?st=7d2f5e8 with Data Recovery

http://www.pixelvaultlib.com/stock-illustration-5318890-laptop.php?st=e14b7c9

I don't know but I have less than 40 hours to do this...

Been extented for another 50 hours cause they stuffed up also I have just opened a logo one as well.

Reason: As the publisher stuffed up with my account I now have an extra 50 hours !!

please note increased payment, this may increase again.

Reason: Not ment to finish for another 18 hours !!!!!!

Keep Going !!!!

only 5 hours left before it has to be at the printers !!!!

• only have 40 hours left from now. it must be in by 7am Monday 30th western aussie time. (not eastern aussie time)
• A 3D look
Colors like dark blue, bright yellow black and dark red.
modern look
modern font ie..HandelGothicBT etc

```html
<!DOCTYPE html>
<html lang="en">
<head>
<meta charset="utf-8">
<title>Salt Pan Computers – 24/7 Computer Services</title>
<link rel="stylesheet" href="https://fonts.googleapis.com/css2?family=Archivo+Black&family=Jost:wght@600;700&family=Fira+Sans:wght@600;700&display=swap">
<style>
  :root {
    --yellow: #fff200;
    --navy: #0a1f8a;
    --navy-deep: #07166a;
    --red: #e3221f;
    --red-deep: #8c0f0c;
    --white: #ffffff;
    --ink: #1a1a1a;
    --shadow: rgba(0, 0, 0, 0.45);
  }
  html, body {
    margin: 0;
    padding: 0;
    overflow: hidden;
    background: #ffffff;
  }
  .advert {
    position: relative;
    width: 840px;
    height: 1200px;
    overflow: hidden;
    background: var(--yellow);
  }
  .advert__shapes {
    position: absolute;
    inset: 0;
  }
  .headline text {
    font-family: "Archivo Black", "Arial Black", sans-serif;
  }
  .service-title text {
    font-family: "Jost", "Trebuchet MS", sans-serif;
    font-weight: 700;
    letter-spacing: 1px;
  }
  .logo-slot {
    position: absolute;
    left: 340px;
    top: 66px;
    width: 420px;
    text-align: center;
    font-family: "Jost", "Trebuchet MS", sans-serif;
    font-weight: 700;
    font-size: 42px;
    letter-spacing: 1px;
    color: var(--navy);
  }
  .service-list {
    position: absolute;
    left: 38px;
    top: 716px;
    margin: 0;
    padding: 0;
    list-style: none;
    font-family: "Fira Sans", "Segoe UI", sans-serif;
    font-weight: 600;
    font-size: 28px;
    line-height: 40px;
    color: var(--navy);
  }
  .service-list li {
    position: relative;
    padding-left: 26px;
  }
  .service-list li::before {
    content: "•";
    position: absolute;
    left: 2px;
    color: var(--red);
  }
  .service-list .wrap {
    display: block;
    line-height: 34px;
    padding-left: 10px;
  }
  .contact-email,
  .contact-web {
    position: absolute;
    left: 40px;
    margin: 0;
    white-space: nowrap;
    font-family: "Fira Sans", "Segoe UI", sans-serif;
  }
  .contact-email {
    top: 966px;
    font-size: 42.5px;
    font-weight: 600;
    color: var(--navy);
  }
  .contact-web {
    top: 1024px;
    font-size: 40px;
    font-weight: 700;
    letter-spacing: 0.6px;
    color: var(--red);
  }
  .phone-band {
    position: absolute;
    left: 0;
    top: 1087px;
    width: 840px;
    height: 113px;
    background: var(--navy);
  }
  .phone-band svg {
    display: block;
  }
  .phone-band text {
    font-family: "Jost", "Trebuchet MS", sans-serif;
    font-weight: 700;
  }
</style>
</head>
<body>
<main class="advert">
  <svg class="advert__shapes" width="840" height="1200" viewBox="0 0 840 1200" aria-hidden="false">
    <defs>
      <filter id="soft-drop" x="-20%" y="-20%" width="140%" height="140%">
        <feDropShadow dx="4" dy="5" stdDeviation="5" flood-color="#000" flood-opacity="0.45"/>
      </filter>
      <radialGradient id="receptionist-tones" cx="50%" cy="45%" r="60%">
        <stop offset="0%" stop-color="#f1d2bb"/>
        <stop offset="55%" stop-color="#d9b78f"/>
        <stop offset="100%" stop-color="#f4f4f4"/>
      </radialGradient>
      <radialGradient id="drive-tones" cx="50%" cy="50%" r="60%">
        <stop offset="0%" stop-color="#b9bcc2"/>
        <stop offset="60%" stop-color="#6b6f78"/>
        <stop offset="100%" stop-color="#e9e9ec"/>
      </radialGradient>
    </defs>

    <!-- blue field -->
    <path class="field-blue" filter="url(#soft-drop)" fill="var(--navy)"
      d="M0 0 H705 C718 210 640 470 432 620 C320 690 140 700 0 680 Z"/>

    <!-- red field -->
    <circle class="field-red" cx="702" cy="663" r="303" fill="var(--red)"
      stroke="var(--red-deep)" stroke-width="3" filter="url(#soft-drop)"/>

    <!-- logo bubble -->
    <circle class="logo-bubble" cx="580" cy="-62" r="312" fill="var(--white)" filter="url(#soft-drop)"/>

    <!-- receptionist photo -->
    <circle cx="175" cy="170" r="106" fill="var(--white)" filter="url(#soft-drop)"/>
    <circle class="photo-receptionist" cx="175" cy="170" r="100" fill="url(#receptionist-tones)"
      role="img" aria-label="Smiling support receptionist wearing a headset"/>

    <!-- drive service photo -->
    <circle cx="660" cy="396" r="84" fill="var(--white)" filter="url(#soft-drop)"/>
    <circle class="photo-drive" cx="660" cy="396" r="79" fill="url(#drive-tones)"
      role="img" aria-label="Gloved hands servicing an open hard disk drive"/>

    <!-- 24/7 -->
    <g class="headline">
      <text x="52" y="474" font-size="240" fill="#000" opacity="0.7" textLength="530" lengthAdjust="spacingAndGlyphs">24/7</text>
      <text x="44" y="466" font-size="240" fill="var(--yellow)" textLength="530" lengthAdjust="spacingAndGlyphs">24/7</text>
    </g>

    <!-- computer services -->
    <g class="service-title">
      <text x="45" y="556" font-size="64" fill="#000" opacity="0.75" textLength="412" lengthAdjust="spacingAndGlyphs">COMPUTER</text>
      <text x="41" y="552" font-size="64" fill="var(--white)" textLength="412" lengthAdjust="spacingAndGlyphs">COMPUTER</text>
      <text x="45" y="624" font-size="64" fill="#000" opacity="0.75" textLength="345" lengthAdjust="spacingAndGlyphs">SERVICES</text>
      <text x="41" y="620" font-size="64" fill="var(--white)" textLength="345" lengthAdjust="spacingAndGlyphs">SERVICES</text>
    </g>

    <!-- all computer problems solved -->
    <g class="headline">
      <text x="566" y="648" font-size="160" fill="var(--ink)" textLength="226" lengthAdjust="spacingAndGlyphs">All</text>
      <text x="560" y="642" font-size="160" fill="var(--yellow)" textLength="226" lengthAdjust="spacingAndGlyphs">All</text>
      <text x="446" y="718" font-size="62" fill="var(--ink)" textLength="350" lengthAdjust="spacingAndGlyphs">Computer</text>
      <text x="442" y="714" font-size="62" fill="var(--yellow)" textLength="350" lengthAdjust="spacingAndGlyphs">Computer</text>
      <text x="456" y="785" font-size="62" fill="var(--ink)" textLength="340" lengthAdjust="spacingAndGlyphs">Problems</text>
      <text x="452" y="781" font-size="62" fill="var(--yellow)" textLength="340" lengthAdjust="spacingAndGlyphs">Problems</text>
      <text x="564" y="852" font-size="62" fill="var(--ink)" textLength="232" lengthAdjust="spacingAndGlyphs">Solved</text>
      <text x="560" y="848" font-size="62" fill="var(--yellow)" textLength="232" lengthAdjust="spacingAndGlyphs">Solved</text>
    </g>
  </svg>

  <div class="logo-slot">LOGO IN HERE</div>

  <ul class="service-list">
    <li>Virus's Removed</li>
    <li>Data Recovery</li>
    <li>Custom Computers<span class="wrap">&amp; Programs built</span></li>
    <li>Picked up &amp; Dropped off</li>
    <li>Private and Business Welcome</li>
  </ul>

  <p class="contact-email">info@saltpancomputers.com.au</p>
  <p class="contact-web">SALTPANCOMPUTERS.COM.AU</p>

  <div class="phone-band">
    <svg width="840" height="113" viewBox="0 0 840 113">
      <text x="46" y="97" font-size="100" fill="#000" opacity="0.6" textLength="748" lengthAdjust="spacingAndGlyphs">0400 13 8562</text>
      <text x="41" y="92" font-size="100" fill="var(--white)" textLength="748" lengthAdjust="spacingAndGlyphs">0400 13 8562</text>
    </svg>
  </div>
</main>
</body>
</html>
```